Counseling Practice Business Card

I need a professional looking business card incorporating my new logo that was just completed. Card needs to incorporate my name and title, description of my specialty, my address, my phone number, my fax number, my email and my website URL. I need to be able to choose design on/with different paper colors and textures.
I do not have a lot of business card ideas so I am open to anything but I want bold,sharp, clear card without additional designs other than my logo (see attached file info). I am open to different color backgrounds or paper colors including black. I do not like traditional brackets around area codes in phone number or dashes between numbers in phone number. Am open to other ways of presenting including periods between numbers as appropriate. I do not know enough to know what I like yet but I want card to coordinate and work together with my logo. My practice emphasizes natural mental health interventions so any use of color (with background paper color or the blue and green in my logo) that elicits nature is nice. In addition to black, any natural brown or wood looking background might be desirable also. Most of the offerings so far look very similar and boring.

Target Market(s)

Potential therapy clients and other professionals

Contact Information for Business Card

Card information:
Gerald P. Whitcombe, Ph.D.
Licensed Clinical Psychologist
Integrative Health Coach
5214 Ambergate Blvd NW
Suite 815
Duluth, GA 30096
(770) 555-0143 phone
(770) 555-0178 fax
drgeraldwhitcombe@examplemail.net
brightpathwellness.example

Font styles to use
Serif
Sans Serif
Other font styles liked:
• anything that you think looks crisp, clear and easily readable

Requirements
Must have
• Any color used should coordinate with my logo design (see attached files).
• Card should be printed horizontally so top and bottom are longest sides of rectangle.
• Background color or paper color should complement and highlight logo. Do not like a white background. black, grey, brown or any color my logo would blend well with.
Nice to have
• I would like designer to utilize color to highlight letters/name or phone-fax-web symbols.
• Bottom edge of card could be highlighted if appropriate to an idea.
Should not have
• I would NOT want the card to have a pure white background at all.
• No clear cards.
• Cards should be oriented with long sides on bottom and top, NOT sides. DO NOT LIKE THIS THIN TALL ORIENTATION.

```html
<!DOCTYPE html>
<html lang="en">
<head>
<meta charset="utf-8">
<title>BrightPath Wellness Business Card</title>
<link rel="stylesheet" href="https://fonts.googleapis.com/css2?family=Open+Sans:wght@400;600;700&display=swap">
<style>
  :root {
    --green: #006837;
    --blue: #2a75bb;
    --ink: #1c1c1a;
    --paper: #ecebe4;
    --stage: #ffffff;
  }
  * { box-sizing: border-box; margin: 0; padding: 0; }
  html, body { width: 1200px; height: 720px; overflow: hidden; background: var(--stage); }
  body { position: relative; font-family: "Open Sans", Arial, sans-serif; color: var(--ink); }

  .card {
    position: absolute;
    width: 444px;
    height: 274px;
    background: var(--paper);
    box-shadow: 8px 10px 14px rgba(0,0,0,0.35);
    overflow: hidden;
  }
  .card--front { left: 106px; top: 208px; }
  .card--back  { left: 646px; top: 206px; }

  .edge-band {
    position: absolute; left: 0; bottom: 0; width: 100%; height: 10px; display: flex;
  }
  .edge-band__green { flex: 1; background: var(--green); }
  .edge-band__blue  { flex: 1; background: var(--blue); }

  .brand {
    position: absolute;
    color: var(--green);
    font-weight: 700;
    text-align: center;
    line-height: 1;
  }
  .brand__name { display: block; letter-spacing: -0.5px; }
  .brand__tag  { display: block; letter-spacing: 0.38em; }

  .card--front .brand { left: 0; width: 100%; top: 100px; }
  .card--front .brand__name { font-size: 52px; }
  .card--front .brand__tag  { font-size: 17px; margin-top: 8px; padding-left: 0.38em; }

  .card--back .brand { left: 14px; width: 192px; top: 116px; }
  .card--back .brand__name { font-size: 30px; }
  .card--back .brand__tag  { font-size: 10px; margin-top: 6px; padding-left: 0.38em; }

  .contact { position: absolute; left: 256px; top: 83px; right: 0; }
  .contact__name { font-size: 11px; font-weight: 400; line-height: 14px; }
  .contact__title { font-size: 6.4px; line-height: 9px; white-space: nowrap; }
  .contact__rule { height: 2px; background: var(--blue); margin-top: 1px; }
  .contact__address { margin-top: 12px; font-size: 8.6px; font-weight: 600; line-height: 12px; }
  .contact__list { list-style: none; font-size: 8.6px; font-weight: 600; line-height: 12px; }
  .contact__list--phone { margin-top: 10px; }
  .contact__list--web { margin-top: 8px; }
  .contact__list li { display: flex; align-items: center; gap: 5px; white-space: nowrap; }
  .contact__list svg { width: 9px; height: 9px; flex: none; }
</style>
</head>
<body>

<section class="card card--front" aria-label="Card front">
  <div class="brand">
    <span class="brand__name">BrightPath</span>
    <span class="brand__tag">WELLNESS</span>
  </div>
  <div class="edge-band"><span class="edge-band__green"></span><span class="edge-band__blue"></span></div>
</section>

<section class="card card--back" aria-label="Card back">
  <div class="brand">
    <span class="brand__name">BrightPath</span>
    <span class="brand__tag">WELLNESS</span>
  </div>

  <div class="contact">
    <p class="contact__name">Gerald P. Whitcombe, Ph.D.</p>
    <p class="contact__title">Licensed Clinical Psychologist / Integrative Health Coach</p>
    <div class="contact__rule"></div>
    <p class="contact__address">5214 Ambergate Blvd NW Suite 815<br>Duluth, GA 30096</p>

    <ul class="contact__list contact__list--phone">
      <li>
        <svg viewBox="0 0 10 10" aria-hidden="true"><path fill="#006837" d="M2 0.5l1.6 2.2-1 1c0.6 1.3 1.5 2.2 2.8 2.8l1-1 2.2 1.6-1 1.9C4.5 9 1 5.5 0.5 2.2z"/></svg>
        770 555 0143
      </li>
      <li>
        <svg viewBox="0 0 10 10" aria-hidden="true"><g fill="none" stroke="#006837" stroke-width="1.2"><rect x="2.5" y="0.8" width="5" height="3"/><rect x="0.8" y="3.8" width="8.4" height="3.6"/><rect x="2.5" y="6.2" width="5" height="3"/></g></svg>
        770 555 0178
      </li>
    </ul>

    <ul class="contact__list contact__list--web">
      <li>
        <svg viewBox="0 0 10 10" aria-hidden="true"><g fill="none" stroke="#006837" stroke-width="1"><circle cx="5" cy="5" r="4.2"/><ellipse cx="5" cy="5" rx="1.8" ry="4.2"/><line x1="0.8" y1="5" x2="9.2" y2="5"/><line x1="1.5" y1="2.8" x2="8.5" y2="2.8"/><line x1="1.5" y1="7.2" x2="8.5" y2="7.2"/></g></svg>
        drgeraldwhitcombe@examplemail.net
      </li>
      <li>
        <svg viewBox="0 0 10 10" aria-hidden="true"><g fill="none" stroke="#006837" stroke-width="1"><rect x="0.6" y="1.8" width="8.8" height="6.4"/><polyline points="0.6,1.8 5,5.6 9.4,1.8"/></g></svg>
        brightpathwellness.example
      </li>
    </ul>
  </div>

  <div class="edge-band"><span class="edge-band__green"></span><span class="edge-band__blue"></span></div>
</section>

</body>
</html>
```